Cd Cover design for Chicago based record label.

Cd Cover design for a new single! Song is dedicated to exotic dancers. We do not want our artist pictures on this one. So please use your imagination. Song Title: "Velvet Hours". Thanks? Artist: Ray Castellan feat. Lil Trevane.

```html
<!DOCTYPE html>
<html lang="en">
<head>
<meta charset="utf-8">
<title>Velvet Hours – Ray Castellan feat. Lil Trevane</title>
<link rel="stylesheet" href="https://fonts.googleapis.com/css2?family=Michroma&family=Kaushan+Script&display=swap">
<style>
  :root {
    --night: #05090f;
    --navy: #0c1a2c;
    --steel-blue: #27456b;
    --glow: #8fc4ff;
    --title-white: #ffffff;
  }
  html, body {
    margin: 0;
    padding: 0;
    width: 1200px;
    height: 1200px;
    overflow: hidden;
    background: var(--night);
  }
  .cover {
    position: relative;
    width: 1200px;
    height: 1200px;
    overflow: hidden;
  }
  .club-backdrop {
    position: absolute;
    inset: 0;
    background:
      radial-gradient(ellipse 70% 28% at 50% 20%, rgba(39,69,107,0.55), transparent 70%),
      radial-gradient(ellipse 60% 22% at 50% 88%, rgba(39,69,107,0.5), transparent 70%),
      radial-gradient(ellipse 80% 40% at 50% 48%, var(--navy), transparent 80%),
      linear-gradient(180deg, #0a1524 0%, var(--night) 50%, #0a1524 100%);
  }
  .title-art {
    position: absolute;
    left: 0;
    top: 0;
    width: 1200px;
    height: 1200px;
  }
  .song-title {
    font-family: "Michroma", sans-serif;
    font-size: 150px;
    fill: var(--title-white);
  }
  .credit-line {
    position: absolute;
    left: 0;
    right: 0;
    top: 680px;
    margin: 0;
    text-align: center;
    font-family: "Kaushan Script", cursive;
    font-size: 62px;
    color: var(--title-white);
    letter-spacing: -1px;
  }
</style>
</head>
<body>
  <main class="cover">
    <div class="club-backdrop" role="img" aria-label="Dark blue-tinted photo of an empty nightclub with rows of ceiling lights reflected on a glossy floor"></div>
    <svg class="title-art" viewBox="0 0 1200 1200" xmlns="http://www.w3.org/2000/svg">
      <defs>
        <filter id="spark-glow" x="-10%" y="-50%" width="120%" height="200%">
          <feGaussianBlur in="SourceAlpha" stdDeviation="9" result="blur"/>
          <feFlood flood-color="#8fc4ff" flood-opacity="0.9"/>
          <feComposite in2="blur" operator="in" result="halo"/>
          <feMerge>
            <feMergeNode in="halo"/>
            <feMergeNode in="halo"/>
            <feMergeNode in="SourceGraphic"/>
          </feMerge>
        </filter>
      </defs>
      <text class="song-title" x="600" y="660" text-anchor="middle" textLength="1096" lengthAdjust="spacingAndGlyphs" filter="url(#spark-glow)">VELVET HOURS</text>
    </svg>
    <p class="credit-line">Ray Castellan feat. Lil Trevane</p>
  </main>
</body>
</html>
```